New design of old website

We need a new design of our domain name reseller website.

kavirnodo.com

we would also like new design for Logo and all.

the site will be in English and portuguesse,

Domain

```html
<!DOCTYPE html>
<html lang="en">
<head>
<meta charset="utf-8">
<title>kavirnodo.com – This Domain Is For Sale</title>
<link href="https://fonts.googleapis.com/css2?family=Arimo:wght@400;700&display=swap" rel="stylesheet">
<style>
:root{
  --page:#ffffff;
  --band:#efefef;
  --rule:#dcdcdc;
  --ink:#333333;
  --muted:#555555;
  --accent:#15b4ea;
  --accent-soft:#cdeef9;
  --note:#e6e6e6;
  --note-sale:#f8d3cf;
}
*{box-sizing:border-box;margin:0;padding:0}
html,body{width:1200px;height:896px;overflow:hidden;background:var(--page)}
body{position:relative;font-family:"Arimo",Arial,sans-serif;color:var(--ink)}
.top-rule{position:absolute;left:18px;top:38px;width:1147px;height:1px;background:var(--rule)}

.notes{position:absolute;left:0;top:0;width:1200px;height:230px}
.note{position:absolute;height:16px;background:var(--note);border-radius:3px}
.note--sale{background:var(--note-sale);height:26px}
.pointers{position:absolute;left:0;top:0}

.site-name{position:absolute;left:0;width:1200px;top:162px;text-align:center;font-size:40px;font-weight:700;line-height:48px;color:var(--ink)}

.band{position:absolute;left:18px;top:229px;width:1147px;height:445px;background:var(--band)}
.headline{position:absolute;left:408px;top:248px;width:410px;height:26px;background:#fff;
  font-size:11px;font-weight:700;text-align:center;line-height:26px;color:#222}
.pitch{position:absolute;left:0;width:1200px;top:286px;text-align:center;font-size:11px;line-height:20px;color:var(--muted)}
.pitch strong{font-size:13px;color:var(--ink);letter-spacing:.5px}

.btn{position:absolute;top:339px;height:34px;font-size:14px;font-weight:700;line-height:34px;text-align:center;border-radius:2px}
.btn--buy{left:467px;width:155px;background:var(--accent);color:#fff}
.btn--buy s{color:#1d3d55;margin:0 4px}
.btn--offer{left:632px;width:113px;background:#fff;color:var(--accent);border:1px solid #e2e2e2}

.stats{position:absolute;left:283px;top:408px;width:651px;height:246px;background:#fff;border:1px solid #d6d6d6;box-shadow:0 2px 3px rgba(0,0,0,.08)}
.stats__title{position:absolute;left:15px;top:13px;font-size:12px;font-weight:700;color:var(--accent)}
.stats__sub{position:absolute;left:15px;top:37px;font-size:10px;color:var(--ink)}
.chart{position:absolute;left:12px;top:58px}
.quick{position:absolute;left:459px;top:34px;width:176px;font-size:10px}
.quick h3{font-size:10px;font-weight:700}
.quick p{margin-top:6px;line-height:14px;color:var(--ink)}
.quick ul{list-style:none;margin-top:6px;border-top:1px solid #e4e4e4}
.quick li{height:20px;line-height:20px;border-bottom:1px solid #e4e4e4;font-weight:700;padding-left:20px;position:relative}
.quick li::before{content:"";position:absolute;left:4px;top:5px;width:5px;height:8px;border:solid #222;border-width:0 2px 2px 0;transform:rotate(45deg)}
.quick__actions{margin-top:12px;display:flex;align-items:center;gap:12px}
.mini-buy{background:var(--accent);color:#fff;font-weight:700;padding:0 11px;height:21px;line-height:21px;border-radius:2px}
.mini-offer{color:var(--accent)}

.footer-rule{position:absolute;left:50px;width:1150px;height:1px;background:var(--rule)}
.footer-col{position:absolute;top:704px;font-size:11px;line-height:18px;color:var(--ink)}
.footer-col h4{font-size:13px;font-weight:700;color:var(--accent);margin-bottom:4px}
.col-divider{position:absolute;top:684px;width:1px;height:144px;background:var(--rule)}
.signature{width:92px;height:22px;background:var(--note);border-radius:3px;margin-top:10px}
.related{list-style:none;width:216px}
.related li{height:25px;line-height:25px;border-bottom:1px solid #e6e6e6;padding-left:14px;position:relative}
.related li:last-child{border-bottom:0}
.related li::before{content:">";position:absolute;left:0}
.social{position:absolute;left:900px;top:698px;display:flex;gap:4px}
.social span{width:18px;height:18px;border-radius:50%;background:#2b2b2b}
.tweet{display:flex;gap:10px;margin-top:2px}
.tweet__mark{flex:none;width:18px;height:18px;border-radius:50%;background:var(--accent);margin-top:2px}
.tweet a,.links a{color:var(--accent);text-decoration:none}
.links{position:absolute;left:252px;top:842px;font-size:11px;display:flex;gap:8px}
.copyright{position:absolute;left:252px;top:862px;font-size:11px;color:var(--ink)}
.copyright b{margin:0 10px 0 30px}
</style>
</head>
<body>
<div class="top-rule"></div>

<div class="notes">
  <div class="note" role="img" aria-label="Handwritten note: Quality SEO Rankings" style="left:333px;top:80px;width:150px"></div>
  <div class="note" role="img" aria-label="Handwritten note: Strong Keywords" style="left:506px;top:47px;width:112px"></div>
  <div class="note" role="img" aria-label="Handwritten note: 500+ Backlinks" style="left:640px;top:104px;width:106px"></div>
  <div class="note" role="img" aria-label="Handwritten note: Short URL" style="left:762px;top:50px;width:76px"></div>
  <div class="note note--sale" role="img" aria-label="Handwritten red note: for sale" style="left:790px;top:128px;width:120px"></div>
  <svg class="pointers" width="1200" height="230" viewBox="0 0 1200 230" fill="none" stroke="#b8b8b8" stroke-width="1">
    <path d="M397 102 Q398 130 415 142"/>
    <path d="M565 70 Q570 110 562 160"/>
    <path d="M690 124 Q695 145 692 158"/>
    <path d="M800 72 Q775 90 767 122"/>
  </svg>
</div>

<div class="site-name">kavirnodo</div>

<div class="band"></div>
<div class="headline">This Domain Is For Sale</div>
<p class="pitch"><strong>kavirnodo.com</strong> is a strong, short, memorable brandable name<br>averaging about 1,000 hits per day. This domain could be yours!</p>
<div class="btn btn--buy">Buy Now <s>$200</s> $125</div>
<div class="btn btn--offer">Make an Offer</div>

<section class="stats">
  <h2 class="stats__title">Statistics</h2>
  <div class="stats__sub">Unique Page Views (Last 30 Days)</div>
  <svg class="chart" width="436" height="174" viewBox="0 0 400 160" font-family="Arimo, Arial, sans-serif" font-size="7" fill="#333">
    <g stroke="#e4e4e4" stroke-dasharray="2 2">
      <line x1="35" y1="30" x2="390" y2="30"/><line x1="35" y1="75" x2="390" y2="75"/><line x1="35" y1="121" x2="390" y2="121"/>
      <line x1="213" y1="10" x2="213" y2="143"/>
    </g>
    <polygon fill="var(--accent-soft)" points="35,143 35,26 48,112 60,113 73,11 85,22 97,41 109,37 121,38 134,111 146,100 158,74 171,13 183,30 195,39 207,91 219,121 231,118 243,92 256,41 268,43 280,43 292,45 305,116 317,106 329,13 341,14 353,25 365,16 378,23 390,103 390,143"/>
    <polyline fill="none" stroke="var(--accent)" stroke-width="1.6" points="35,26 48,112 60,113 73,11 85,22 97,41 109,37 121,38 134,111 146,100 158,74 171,13 183,30 195,39 207,91 219,121 231,118 243,92 256,41 268,43 280,43 292,45 305,116 317,106 329,13 341,14 353,25 365,16 378,23 390,103"/>
    <g fill="var(--accent)">
      <circle cx="35" cy="26" r="2"/><circle cx="48" cy="112" r="2"/><circle cx="60" cy="113" r="2"/><circle cx="73" cy="11" r="2"/><circle cx="85" cy="22" r="2"/><circle cx="97" cy="41" r="2"/><circle cx="109" cy="37" r="2"/><circle cx="121" cy="38" r="2"/><circle cx="134" cy="111" r="2"/><circle cx="146" cy="100" r="2"/><circle cx="158" cy="74" r="2"/><circle cx="171" cy="13" r="2"/><circle cx="183" cy="30" r="2"/><circle cx="195" cy="39" r="2"/><circle cx="207" cy="91" r="2"/><circle cx="219" cy="121" r="2"/><circle cx="231" cy="118" r="2"/><circle cx="243" cy="92" r="2"/><circle cx="256" cy="41" r="2"/><circle cx="268" cy="43" r="2"/><circle cx="280" cy="43" r="2"/><circle cx="292" cy="45" r="2"/><circle cx="305" cy="116" r="2"/><circle cx="317" cy="106" r="2"/><circle cx="329" cy="13" r="2"/><circle cx="341" cy="14" r="2"/><circle cx="353" cy="25" r="2"/><circle cx="365" cy="16" r="2"/><circle cx="378" cy="23" r="2"/><circle cx="390" cy="103" r="2"/>
    </g>
    <line x1="35" y1="143" x2="390" y2="143" stroke="#999"/>
    <line x1="35" y1="10" x2="35" y2="143" stroke="#999"/>
    <g text-anchor="end">
      <text x="31" y="32">500</text><text x="31" y="55">400</text><text x="31" y="78">300</text><text x="31" y="101">200</text><text x="31" y="124">100</text><text x="31" y="146">0</text>
    </g>
    <text x="5" y="154">Feb 1 2013</text>
    <text x="213" y="154" text-anchor="middle">Feb 16 2013</text>
    <text x="399" y="154" text-anchor="end">Mar 2 2013</text>
  </svg>
  <div class="quick">
    <h3>Quick Stats (Last 30 Days)</h3>
    <p>These stats are automatically pulled from StatTrack Analytics.</p>
    <ul>
      <li>11,145 Visits</li>
      <li>5,042 Unique Visitors</li>
      <li>27,102 Pageviews</li>
      <li>25.86% New Visits</li>
    </ul>
    <div class="quick__actions"><span class="mini-buy">Buy Now</span><span class="mini-offer">Make an Offer</span></div>
  </div>
</section>

<div class="footer-rule" style="top:682px"></div>
<div class="col-divider" style="left:491px"></div>
<div class="col-divider" style="left:737px"></div>

<div class="footer-col" style="left:260px;width:210px">
  <h4>About Vendra</h4>
  <p>With a widgetized footer, you can customize &nbsp;&nbsp;&nbsp;&nbsp;&nbsp;&nbsp;&nbsp;&nbsp;&nbsp; even further.</p>
  <div class="signature" role="img" aria-label="Handwritten signature of Vendra"></div>
</div>

<div class="footer-col" style="left:507px">
  <h4>Related Domains For Sale</h4>
  <ul class="related">
    <li>VendraShines.com</li>
    <li>SellNamesWell.com</li>
    <li>AnotherFineName.com</li>
  </ul>
</div>

<div class="footer-col" style="left:753px;width:210px">
  <h4>Stay Connected</h4>
  <div class="tweet">
    <span class="tweet__mark"></span>
    <p><b>24 days ago</b> - <a>@LateNightLarsen</a> sounds about like my day man, started at 8 am, ended at 1:45am, over 1500 miles away haha. #workhardplayharder</p>
  </div>
</div>
<div class="social"><span></span><span></span><span></span></div>

<div class="footer-rule" style="top:828px"></div>
<nav class="links"><a>About Us</a><a>Contact Us</a><a>Shortcodes</a></nav>
<p class="copyright">©<b>copyright 2013</b>All Rights Reserved.</p>
</body>
</html>
```